Plumbing Contractor Website Design

We are working with a Plumbing contractor in CA called KT Plumbline.

Some sites to use for content/competitors and inspiration:

https://www.pipevalex.com
https://www.drainmoss.com
https://quillbark.example/web/contractor/ (lots of contractor website designs we've approved and continue to show clients)

Thank you for taking the time to consider designing a website for us. We are web developers based in Stockton, CA, USA. Most of our projects go through the same process. Understanding this process may help you win a project with us. We custom-code all of our websites in-house. We don’t have any requirements as to what tools you use for your design, but we prefer Figma files. For any design that we label as four-stars, we send it to the client for review. The client picks the final design they want us to use. Once we complete this process, we will continue to show additional clients all the four-star sites and purchase them later. Your designs will have multiple chances to sell. For better chances of success, we ask that you follow these guidelines.

IMAGES:
If you use any images or icons in the design, we ask that you have a link to the asset so we can purchase the image/icon. Most of the designs we submit do not have the customer’s images on them unless they have some great images. Be creative; show us the feeling you are trying to portray with your image choices. Use any royalty-free site you choose. We subscribe to Adobe and mainly use their images, but we can purchase images outside of Adobe.

PLEASE NOTE: we will not submit designs to clients with watermarks on the images.

FONTS:
We ask that you identify the fonts used in the design. This can be done in a message if you want. We typically use Google Fonts and Adobe Fonts.

CONTENT:
We're always open to different content and ideas. We often submit designs with stock images so the client can see our vision. We typically take pictures after the website launch to use their images with our vision. Lorem Ipsum is fine for paragraphs, but we ask that you write the headers in correct English. We want to be able to show the vision and identify the sections of the website.

INSPIRATION:
We typically add a couple of links in the brief of websites we like to help you get started in your design.

REVISIONS:
We do not often ask for revisions of the designs unless we see something in the design that may not appeal to the client. If there are slight changes that we want to make, we do that in the development process.

FEEDBACK:
We rarely give feedback on designs during the design process. We are working on many website projects and do not have the time to provide feedback. We usually respond if your request is well thought out and asks specific questions, but a note asking “feedback, please” usually goes unanswered

```html
<!DOCTYPE html>
<html lang="en">
<head>
<meta charset="utf-8">
<title>KT Plumbline – Expert Plumbing &amp; Drain Cleaning</title>
<link rel="stylesheet" href="https://fonts.googleapis.com/css2?family=Roboto+Condensed:wght@400;700&family=Roboto:wght@400;500&display=swap">
<style>
  :root {
    --brand-blue: #2178d4;
    --brand-blue-deep: #1a63b8;
    --heading-navy: #0f4f91;
    --hero-blue: #3d7fb8;
    --hero-light: #c9d7e3;
    --page-bg: #f4f5f7;
    --white: #ffffff;
    --input-hint: #9aa3ad;
    --portrait-top: #dfe5ea;
    --portrait-mid: #9c8a78;
    --portrait-low: #3b4b5f;
  }
  * { box-sizing: border-box; margin: 0; padding: 0; }
  html, body { width: 1200px; height: 675px; overflow: hidden; }
  body {
    background: var(--page-bg);
    font-family: "Roboto", Arial, sans-serif;
    color: var(--white);
    position: relative;
  }

  /* Header */
  .site-header {
    position: absolute; left: 0; top: 0; width: 1200px; height: 96px;
    background: var(--brand-blue);
    display: flex; align-items: center;
    padding: 0 60px;
    z-index: 3;
  }
  .brand { display: flex; align-items: center; gap: 10px; width: 230px; }
  .brand-dot { width: 22px; height: 22px; border-radius: 50%; background: var(--white); }
  .brand-name {
    font-family: "Roboto Condensed", Arial, sans-serif;
    font-weight: 700; font-size: 20px; color: var(--white); letter-spacing: .5px;
  }
  .main-nav { display: flex; gap: 16px; margin-left: 90px; }
  .main-nav a {
    color: var(--white); text-decoration: none; font-size: 14px;
    font-family: "Roboto Condensed", Arial, sans-serif;
  }
  .header-contact { margin-left: auto; display: flex; flex-direction: column; align-items: center; gap: 4px; }
  .header-contact .locator {
    font-family: "Roboto Condensed", Arial, sans-serif; font-weight: 700;
    font-size: 14px; text-decoration: underline; color: var(--white);
  }
  .header-contact .phone {
    font-family: "Roboto Condensed", Arial, sans-serif; font-size: 20px; color: var(--white);
  }
  .btn-schedule {
    margin-top: 2px;
    background: var(--white); color: var(--brand-blue-deep);
    font-size: 12px; padding: 8px 20px; border-radius: 14px;
  }

  /* Hero */
  .hero {
    position: absolute; left: 0; top: 96px; width: 1200px; height: 372px;
    background: linear-gradient(90deg, var(--hero-blue) 0%, #5f93c1 30%, #98b6d0 50%, var(--hero-light) 62%);
    overflow: hidden;
  }
  .hero-portrait {
    position: absolute; right: 0; top: 0; width: 520px; height: 372px;
    background:
      linear-gradient(180deg, var(--portrait-top) 0%, #cfc7bd 28%, var(--portrait-mid) 55%, var(--portrait-low) 100%);
  }
  .hero-copy { position: absolute; left: 88px; top: 56px; width: 480px; }
  .hero-title {
    font-family: "Roboto Condensed", Arial, sans-serif; font-weight: 700;
    font-size: 34px; line-height: 1.15; text-transform: uppercase;
  }
  .hero-text { margin-top: 14px; font-size: 11px; line-height: 1.45; width: 330px; }
  .locator-form { margin-top: 16px; }
  .locator-form label {
    display: block; font-family: "Roboto Condensed", Arial, sans-serif; font-weight: 700;
    font-size: 15px; text-transform: uppercase; margin-bottom: 8px;
  }
  .locator-row { display: flex; align-items: center; gap: 10px; }
  .locator-input {
    width: 380px; height: 36px; border-radius: 18px; background: var(--white);
    color: var(--input-hint); font-size: 11px; padding: 0 18px; display: flex; align-items: center;
  }
  .btn-submit {
    width: 104px; height: 38px; border-radius: 19px; background: var(--brand-blue);
    color: var(--white); font-size: 12px; display: flex; align-items: center; justify-content: center;
  }

  /* Services */
  .services { position: absolute; left: 0; top: 468px; width: 1200px; height: 207px; }
  .services-title {
    margin-top: 44px; text-align: center;
    font-family: "Roboto Condensed", Arial, sans-serif; font-weight: 700;
    font-size: 34px; color: var(--heading-navy); text-transform: uppercase;
  }
  .service-cards { position: absolute; left: 100px; top: 110px; display: flex; gap: 14px; }
  .service-card {
    position: relative; width: 230px; height: 120px; border-radius: 12px 12px 0 0; overflow: hidden;
  }
  .service-card .badge {
    position: absolute; left: 50%; bottom: -22px; transform: translateX(-50%);
    width: 44px; height: 44px; border-radius: 50%; background: var(--brand-blue);
  }
  .card-fixtures { background: linear-gradient(135deg, #c9ced6, #7f8896); }
  .card-pipes { background: linear-gradient(135deg, #e4e7ea, #b7bcc2); }
  .card-kitchen { background: linear-gradient(135deg, #9c9a95, #e6e3de); }
  .card-boiler { background: linear-gradient(135deg, #7c3a34, #c9c3bd); }
</style>
</head>
<body>
  <header class="site-header">
    <div class="brand">
      <span class="brand-dot"></span>
      <span class="brand-name">KT PLUMBLINE</span>
    </div>
    <nav class="main-nav">
      <a href="#">Schedule service</a>
      <a href="#">Locations</a>
      <a href="#">Plumbing &amp; Drains</a>
      <a href="#">Emergency Plumbing</a>
      <a href="#">About us</a>
    </nav>
    <div class="header-contact">
      <span class="locator">FIND YOUR LOCAL PLUMBER</span>
      <span class="phone">+(833) 555-0142</span>
      <span class="btn-schedule">Schedule online</span>
    </div>
  </header>

  <section class="hero" role="img" aria-label="Bright modern kitchen with sink, softly blurred behind a blue overlay">
    <div class="hero-portrait" role="img" aria-label="Smiling plumber in plaid shirt and overalls holding a blue clipboard"></div>
    <div class="hero-copy">
      <h1 class="hero-title">We provide expert plumbing<br>&amp; drain cleaning services</h1>
      <p class="hero-text">Lorem ipsum dolor sit amet, consectetur adipiscing elit, sed do eiusmod tempor incididunt ut labore et dolore magna aliqua. Ut enim ad minim veniam, quis nostrud exercitation ullamco laboris nisi ut aliquip ex ea commodo consequat.</p>
      <div class="locator-form">
        <label>Find your local plumber</label>
        <div class="locator-row">
          <div class="locator-input">Enter Zip, City or Postal code</div>
          <div class="btn-submit">Submit</div>
        </div>
      </div>
    </div>
  </section>

  <section class="services">
    <h2 class="services-title">Our services</h2>
    <div class="service-cards">
      <div class="service-card card-fixtures" role="img" aria-label="Plumber fitting bathroom pipes and fixtures"><span class="badge"></span></div>
      <div class="service-card card-pipes" role="img" aria-label="Wrench tightening a sink drain trap"><span class="badge"></span></div>
      <div class="service-card card-kitchen" role="img" aria-label="Plumber working under a kitchen sink cabinet"><span class="badge"></span></div>
      <div class="service-card card-boiler" role="img" aria-label="Technician in a blue cap servicing a water heater"><span class="badge"></span></div>
    </div>
  </section>
</body>
</html>
```